Custom Wordpress Theme - Original and Professional

We are a Harbourline IT Consulting firm that provide small and medium business in Australia three different levels of IT service.
We are looking for a developer who will create a customised, original and professional wordpress theme. We are looking for the developer to create a professional, clean, clear and simple theme with a stylish layout, images and icons.
Our three services are: IT support | IT Services | IT Solutions and we would like to clearly differentiate the difference in each level of service in as few words as possible.
IT Support is the ad hock “call us, when you need us” service, that smaller business or those with minimal issues use.
IT service is the unlimited service, that business with existing (and well maintained) IT systems choose and is both flexible and scalable including no contracts or paperwork required.
IT solutions are the unlimited service that businesses that need new or updated infrastructure choose and it includes all the hardware, software and services with no contracts or any ongoing commitment.
The main page on the web site will attract the visitor to choose the right “service level” for their business and then we will have a dedicated page for each service and another page for a comparison (table) to compare all three services.
Lastly we will need a contact us page that has both office locations (Sydney and Melbourne), contact phone numbers and an email form.
Items we are focused on for this project are: 1. Images, 2.Icons 3. Layout.
In summary we are looking for a custom WordPress theme into a 6 page (Home, IT Support, IT Services, IT Solutions, Compare Service levels and Contact us) website. The design must include relevant images and icons and be clear, simple, professional and sleek.

Thank you for your time and creativity and I look forward to working with you!

Target Market(s)

Small and Medium businesses in Australia

Industry/Entity Type

Boutique

Requirements
Must have
• - 6 Pages layout: Home, IT support, IT services, IT Solutions, Compare service levels and Contact us
- Images, Layout and Icons.
- Clean, Clear, Simple, Elegant, Stylish.
Nice to have
• - Some text (if possible but not required).
Should not have
• - Complexity.
- Confusing layout.
- Generic non matching images and icons.

```html
<!DOCTYPE html>
<html lang="en">
<head>
<meta charset="utf-8">
<title>Harbourline IT Consulting</title>
<link href="https://fonts.googleapis.com/css2?family=Bebas+Neue&family=Roboto+Condensed:wght@300;400;700&display=swap" rel="stylesheet">
<style>
:root{
  --navy:#1d5575;
  --navy-deep:#174866;
  --band:#1c5170;
  --nav:#6a8ea9;
  --grey-text:#7f8a93;
  --sky-light:#eef3f8;
  --sky-mid:#c9d9e8;
  --sky-deep:#4f86bb;
  --white:#ffffff;
}
*{margin:0;padding:0;box-sizing:border-box}
html,body{width:1200px;height:1114px;overflow:hidden;background:var(--white)}
body{font-family:"Roboto Condensed",Arial,sans-serif;position:relative}
.display{font-family:"Bebas Neue","Roboto Condensed",sans-serif}

/* header */
.site-header{position:absolute;left:0;top:0;width:1200px;height:121px;
  background:linear-gradient(100deg,#fff 0%,#f3f6fa 55%,#d6e3ef 85%,#b9cfe4 100%)}
.brand{position:absolute;left:163px;top:24px;display:flex;align-items:center;gap:14px}
.brand-mark{width:70px;height:70px;background:var(--navy)}
.brand-name{font-family:"Bebas Neue",sans-serif;font-size:44px;line-height:1;color:var(--navy);letter-spacing:1px}
.help{position:absolute;right:171px;top:26px;text-align:right;display:flex;align-items:flex-end;gap:8px}
.help-label{font-family:"Bebas Neue",sans-serif;font-size:21px;color:#2f7fb0;line-height:1}
.help-number{font-family:"Bebas Neue",sans-serif;font-size:36px;color:var(--navy);line-height:1}

/* navigation */
.main-nav{position:absolute;left:0;top:121px;width:1200px;height:44px;
  background:linear-gradient(90deg,#7d9db5,#5f86a4 60%,#3f6f98)}
.main-nav ul{list-style:none;position:absolute;left:192px;top:0;height:44px;display:flex;align-items:center}
.main-nav li{font-family:"Bebas Neue",sans-serif;font-size:20px;color:#fff;letter-spacing:.4px;display:flex;align-items:center}
.main-nav li+li::before{content:"";display:inline-block;width:2px;height:18px;background:#fff;margin:0 22px 0 24px}

/* hero */
.hero{position:absolute;left:0;top:165px;width:1200px;height:423px;overflow:hidden}
.hero-backdrop{position:absolute;inset:0;
  background:
   radial-gradient(circle at 370px 240px,#eef9fb 0,#d7ecf3 130px,rgba(215,230,240,.4) 280px,transparent 300px),
   linear-gradient(110deg,#f2f5f9 0%,#e4ebf2 45%,#c8d8e8 68%,#5a8dc0 80%,#d7e2ed 92%,#eef2f6 100%)}
.hero-portrait{position:absolute;left:704px;top:13px;width:237px;height:410px;
  background:linear-gradient(180deg,#c9ced6 0%,#3f63b2 35%,#2c4f9c 75%,#2b2f38 100%);border-radius:90px 90px 0 0}
.hero-kicker{position:absolute;left:192px;top:98px;font-weight:300;font-size:38px;color:var(--grey-text);line-height:1}
.hero-title{position:absolute;left:190px;top:132px;font-size:82px;color:var(--navy);line-height:1;letter-spacing:.5px}
.hero-sub{position:absolute;left:192px;top:207px;font-weight:400;font-size:36px;color:var(--navy);line-height:1}
.cta{position:absolute;left:195px;top:258px;width:390px;height:99px;border-radius:4px;
  background:linear-gradient(180deg,#2f74a0 0%,#1d5b85 45%,#103f60 100%);
  box-shadow:0 0 0 2px #4a91bd inset,0 3px 6px rgba(0,0,0,.25);color:#fff;text-align:center}
.cta-label{display:block;font-family:"Bebas Neue",sans-serif;font-size:26px;padding-top:9px;line-height:1}
.cta-number{display:block;font-family:"Bebas Neue",sans-serif;font-size:66px;line-height:1;margin-top:2px}

/* service tiles */
.services{position:absolute;left:0;top:588px;width:1200px;height:226px;background:#fff;display:flex;justify-content:center}
.service{position:relative;text-align:center}
.service-icon{position:absolute;left:50%;top:30px;transform:translateX(-50%)}
.service-name{position:absolute;left:0;right:0;top:167px;font-family:"Bebas Neue",sans-serif;font-size:36px;color:var(--navy)}
.service.divided::before{content:"";position:absolute;left:-22px;top:14px;width:22px;height:200px;
  background:linear-gradient(90deg,rgba(0,0,0,0),rgba(0,0,0,.07) 50%,rgba(0,0,0,0))}
.services .service:nth-child(1){width:296px;margin-left:150px}
.services .service:nth-child(2){width:264px;margin-left:22px}
.services .service:nth-child(3){width:300px;margin-left:22px}

/* welcome */
.welcome{position:absolute;left:0;top:814px;width:1200px;height:300px;background:var(--band);overflow:hidden}
.welcome-photo{position:absolute;right:0;top:0;width:420px;height:300px;
  background:linear-gradient(90deg,rgba(28,81,112,1) 0%,rgba(40,100,120,.9) 40%,#2b6577 70%,#235a6f 100%)}
.welcome-title{position:relative;text-align:center;padding-top:92px;font-size:62px;color:#fff;line-height:1;letter-spacing:.5px}
.welcome-text{position:relative;width:656px;margin:16px auto 0;text-align:center;color:#fff;font-weight:300;font-size:19.5px;line-height:22.7px}
</style>
</head>
<body>

<header class="site-header">
  <div class="brand">
    <div class="brand-mark"></div>
    <div class="brand-name">Harbourline IT Consulting</div>
  </div>
  <div class="help">
    <svg width="42" height="44" viewBox="0 0 42 44" aria-hidden="true">
      <path d="M6 24 V19 A15 15 0 0 1 36 19 V24" fill="none" stroke="#1d5575" stroke-width="3.5"/>
      <rect x="2" y="21" width="9" height="14" rx="3" fill="#1d5575"/>
      <rect x="31" y="21" width="9" height="14" rx="3" fill="#1d5575"/>
      <path d="M35 34 Q33 42 22 42" fill="none" stroke="#1d5575" stroke-width="2.5"/>
      <circle cx="21" cy="42" r="2.5" fill="#1d5575"/>
    </svg>
    <div>
      <div class="help-label">Need help call us</div>
      <div class="help-number">1-800-555-0147</div>
    </div>
  </div>
</header>

<nav class="main-nav">
  <ul>
    <li>Home</li><li>IT Support</li><li>IT Services</li><li>IT Solutions</li><li>Compare Service Levels</li><li>Contact Us</li>
  </ul>
</nav>

<section class="hero">
  <div class="hero-backdrop" role="img" aria-label="Soft blue backdrop with a glowing globe and sweeping light curves"></div>
  <div class="hero-portrait" role="img" aria-label="Photo of a consultant in a blue shirt standing with arms crossed"></div>
  <p class="hero-kicker">UT WISI ENIM</p>
  <h1 class="hero-title display">UT DOLOR ADMINIM</h1>
  <p class="hero-sub">LOBORTIS NISL UT ALIQUIP</p>
  <div class="cta">
    <span class="cta-label">Call us now for a consultation</span>
    <span class="cta-number">1-800-555-0147</span>
  </div>
</section>

<section class="services">
  <div class="service">
    <svg class="service-icon" width="120" height="120" viewBox="0 0 120 120" aria-hidden="true">
      <defs>
        <g id="tooth"><rect x="-7" y="-30" width="14" height="14" rx="2"/></g>
      </defs>
      <g fill="#1d5575" transform="translate(44,76)">
        <circle r="24"/>
        <use href="#tooth"/><use href="#tooth" transform="rotate(45)"/><use href="#tooth" transform="rotate(90)"/><use href="#tooth" transform="rotate(135)"/>
        <use href="#tooth" transform="rotate(180)"/><use href="#tooth" transform="rotate(225)"/><use href="#tooth" transform="rotate(270)"/><use href="#tooth" transform="rotate(315)"/>
        <circle r="10" fill="#fff"/>
      </g>
      <g fill="#1d5575" transform="translate(87,30) scale(.72)">
        <circle r="24"/>
        <use href="#tooth"/><use href="#tooth" transform="rotate(45)"/><use href="#tooth" transform="rotate(90)"/><use href="#tooth" transform="rotate(135)"/>
        <use href="#tooth" transform="rotate(180)"/><use href="#tooth" transform="rotate(225)"/><use href="#tooth" transform="rotate(270)"/><use href="#tooth" transform="rotate(315)"/>
        <circle r="10" fill="#fff"/>
      </g>
    </svg>
    <h2 class="service-name">IT Services</h2>
  </div>
  <div class="service divided">
    <svg class="service-icon" width="120" height="120" viewBox="0 0 120 120" aria-hidden="true">
      <ellipse cx="60" cy="56" rx="40" ry="48" fill="#1d5575"/>
      <path d="M20 60 A40 40 0 0 1 100 60" fill="none" stroke="#1d5575" stroke-width="8"/>
      <rect x="12" y="50" width="14" height="26" rx="6" fill="#1d5575"/>
      <rect x="94" y="50" width="14" height="26" rx="6" fill="#1d5575"/>
      <path d="M100 76 Q98 102 70 106" fill="none" stroke="#1d5575" stroke-width="5"/>
      <rect x="58" y="101" width="16" height="10" rx="5" fill="#1d5575"/>
    </svg>
    <h2 class="service-name">IT Support</h2>
  </div>
  <div class="service divided">
    <svg class="service-icon" width="120" height="124" viewBox="0 0 120 124" aria-hidden="true">
      <g stroke="#1d5575" stroke-width="7" stroke-linecap="round">
        <line x1="60" y1="6" x2="60" y2="18"/>
        <line x1="24" y1="20" x2="32" y2="28"/><line x1="96" y1="20" x2="88" y2="28"/>
        <line x1="8" y1="56" x2="20" y2="56"/><line x1="100" y1="56" x2="112" y2="56"/>
        <line x1="24" y1="92" x2="32" y2="84"/><line x1="96" y1="92" x2="88" y2="84"/>
      </g>
      <path d="M60 30 A26 26 0 0 1 78 75 Q72 82 72 90 H48 Q48 82 42 75 A26 26 0 0 1 60 30Z" fill="#1d5575"/>
      <rect x="47" y="94" width="26" height="6" rx="2" fill="#1d5575"/>
      <rect x="49" y="103" width="22" height="6" rx="2" fill="#1d5575"/>
      <path d="M53 112 H67 L63 118 H57Z" fill="#1d5575"/>
    </svg>
    <h2 class="service-name">IT Solutions</h2>
  </div>
</section>

<section class="welcome">
  <div class="welcome-photo" role="img" aria-label="Photo of a smiling support agent wearing a headset, tinted blue"></div>
  <h2 class="welcome-title display">Welcome to Harbourline IT Consulting</h2>
  <p class="welcome-text">Ut wisi enim ad minim veniam, quis nostrud exerci tation ullamcorper suscipit lobortis nisl ut aliquip ex ea commodo consequat. Duis autem vel eum iriure dolor in hendrerit in vulputate velit esse molestie consequat, vel illum dolore eu feugiat nulla facilisis at vero eros et accumsan et iusto odio dignissim qui blandit praesent luptatum zzril delenit augue duis dolore te feugait nulla Ut wisi enim ad minim veniam, quis nostrud exerci tation ullamcorper suscipit lobortis nisl ut aliquip ex ea commodo consequat. Duis autem vel eum iriure dolor in hendrerit in vulputate velit esse molestie consequat.</p>
</section>

</body>
</html>
```